Design a Business Card from pre-existing logo

I have a logo for my company and am looking for a designer to design the business card
I have a basic idea of what i want but new ideas are welcome too!

Am attaching a reference of the front side and the logo to be used.
the front will have a logo and the company name, the back will have a name, designation, phone number , website in very elegant font and clean formatting .... you can experiment with icons if you like(font and background colour needs to match front).

the font on the front needs to be chosen too !
i will need the illustrator/photoshop file too, for later customisation or updating..

```html
<!DOCTYPE html>
<html lang="en">
<head>
<meta charset="utf-8">
<title>Hivelight Studio – Business Card</title>
<link rel="stylesheet" href="https://fonts.googleapis.com/css2?family=Roboto+Condensed:wght@400;700&family=Roboto:wght@400;500&display=swap">
<style>
  :root {
    --stage: #26252b;
    --card-yellow: #ffd400;
    --band-ochre: #c9ab1c;
    --ink: #2a2a2a;
    --ink-soft: #3a3a3a;
  }
  * { box-sizing: border-box; margin: 0; padding: 0; }
  html, body { width: 1200px; height: 848px; overflow: hidden; }
  body {
    background: var(--stage);
    font-family: "Roboto", Arial, sans-serif;
    position: relative;
  }
  .card {
    position: absolute;
    width: 500px;
    height: 286px;
    background: var(--card-yellow);
    color: var(--ink);
  }

  /* Back side: name + contact details */
  .card-back { left: 140px; top: 110px; }
  .card-back .divider-band {
    position: absolute;
    left: 232px;
    top: 0;
    width: 10px;
    height: 100%;
    background: var(--band-ochre);
  }
  .card-back .identity {
    position: absolute;
    left: 0;
    width: 232px;
    top: 50%;
    transform: translateY(-50%);
    padding-left: 38px;
  }
  .card-back .person-name {
    font-family: "Roboto Condensed", "Arial Narrow", sans-serif;
    font-weight: 700;
    font-size: 22px;
    letter-spacing: 0.5px;
    text-transform: uppercase;
    line-height: 1.1;
  }
  .card-back .person-role {
    font-size: 14px;
    color: var(--ink-soft);
    text-align: right;
    padding-right: 22px;
    margin-top: 2px;
  }
  .contact-list {
    position: absolute;
    left: 272px;
    top: 50%;
    transform: translateY(-50%);
    list-style: none;
    display: flex;
    flex-direction: column;
    gap: 14px;
  }
  .contact-item {
    display: flex;
    align-items: center;
    gap: 10px;
    font-size: 12.5px;
    color: var(--ink);
  }
  .contact-icon {
    width: 18px;
    height: 18px;
    flex: none;
  }

  /* Front side: company name */
  .card-front { left: 560px; top: 452px; }
  .brand {
    position: absolute;
    left: 0;
    right: 0;
    top: 96px;
    display: flex;
    align-items: center;
    justify-content: center;
    gap: 12px;
  }
  .brand-dot {
    width: 22px;
    height: 22px;
    border-radius: 50%;
    background: var(--ink);
  }
  .brand-name {
    font-family: "Roboto Condensed", "Arial Narrow", sans-serif;
    font-weight: 700;
    font-size: 38px;
    color: var(--ink);
  }
  .front-web {
    position: absolute;
    left: 0;
    right: 0;
    top: 196px;
    text-align: center;
    font-size: 14px;
    color: var(--ink);
  }
</style>
</head>
<body>

<section class="card card-back" aria-label="Business card back">
  <div class="divider-band"></div>
  <div class="identity">
    <p class="person-name">Miles Carrow</p>
    <p class="person-role">Director</p>
  </div>
  <ul class="contact-list">
    <li class="contact-item">
      <svg class="contact-icon" viewBox="0 0 18 18" aria-hidden="true">
        <rect width="18" height="18" rx="2" fill="#2a2a2a"/>
        <path d="M9 3.5a3.5 3.5 0 0 0-3.5 3.5c0 2.6 3.5 7 3.5 7s3.5-4.4 3.5-7A3.5 3.5 0 0 0 9 3.5zm0 4.9a1.4 1.4 0 1 1 0-2.8 1.4 1.4 0 0 1 0 2.8z" fill="#ffd400"/>
      </svg>
      <span>North street area, Port Avel</span>
    </li>
    <li class="contact-item">
      <svg class="contact-icon" viewBox="0 0 18 18" aria-hidden="true">
        <rect width="18" height="18" rx="2" fill="#2a2a2a"/>
        <path d="M5.2 3.8l2 .2.9 2.6-1.3 1a7 7 0 0 0 3.6 3.6l1-1.3 2.6.9.2 2c-.6.8-1.6 1.2-2.6 1A9.5 9.5 0 0 1 4.2 6.4c-.2-1 .2-2 1-2.6z" fill="#ffd400"/>
      </svg>
      <span>0123 456 7890</span>
    </li>
    <li class="contact-item">
      <svg class="contact-icon" viewBox="0 0 18 18" aria-hidden="true">
        <rect width="18" height="18" rx="2" fill="#2a2a2a"/>
        <rect x="4" y="5.5" width="10" height="7" fill="none" stroke="#ffd400" stroke-width="1.3"/>
        <path d="M4 5.5l5 4 5-4" fill="none" stroke="#ffd400" stroke-width="1.3"/>
      </svg>
      <span>hello@hivelight.studio</span>
    </li>
    <li class="contact-item">
      <svg class="contact-icon" viewBox="0 0 18 18" aria-hidden="true">
        <rect width="18" height="18" rx="2" fill="#2a2a2a"/>
        <circle cx="9" cy="9" r="4.8" fill="none" stroke="#ffd400" stroke-width="1.2"/>
        <ellipse cx="9" cy="9" rx="2" ry="4.8" fill="none" stroke="#ffd400" stroke-width="1"/>
        <path d="M4.2 9h9.6" stroke="#ffd400" stroke-width="1"/>
      </svg>
      <span>www.hivelight.studio</span>
    </li>
  </ul>
</section>

<section class="card card-front" aria-label="Business card front">
  <div class="brand">
    <span class="brand-dot"></span>
    <span class="brand-name">Hivelight Studio</span>
  </div>
  <p class="front-web">www.hivelight.studio</p>
</section>

</body>
</html>
```